Minimalistic logo and website for plovrak.com

My colleague and I just started a new company. We need a website to replace the placeholder at https://plovrak.com/

We need a onepager website. A logotype and color profiles. We like minimalism. Scandinavian design.

Below is just information about the company. You can rearrange it, add photos, emit stuff. Maybe even add stuff if you think it is necessary.

# About Plovrak
Plovrak builds critical applications to capture new markets, create modern services and captivate our customers in new and engaging ways. Creating effective and engaging solutions that truly work has always been Plovrak's core offering and is what makes us excited to work in digital. We are a forward thinking company embracing the opportunities of digital transformation and automations.

# Core services
Business automation
Application development and services for desktop and mobile
Interface Design and UX
Enterprise integrations

# Some more data
Plovrak was founded by Torvald Bergqvist and Mikael Dahlgren in 2021.
Linkedin: https://www.netlinkpro.example/company/74819203/admin/

# Inspiration
Minimal. Simple.
https://www.brunvikformstudio.se/contact

Target Market(s)

Businesses

Industry/Entity Type

IT, business automation, data

Number of Pages Required

1 page

Font styles to use
Sans Serif

Colors

Designer to choose colors to be used in the design.

Requirements
Must have
• Onepage design. Minimalism.
Should not have
• Menus

```html
<!DOCTYPE html>
<html lang="en">
<head>
<meta charset="utf-8">
<title>Plovrak — Digital Transformation</title>
<link rel="stylesheet" href="https://fonts.googleapis.com/css2?family=Archivo:wght@800;900&family=Poppins:wght@300;400;600&family=Roboto:wght@400;500;700&display=swap">
<style>
  :root {
    --ink: #0b0b0b;
    --white: #ffffff;
    --olive-deep: #2c2203;
    --olive: #4a3b08;
    --olive-light: #6b5717;
    --cream: #faf1de;
    --muted: #6e6e6e;
    --brown: #4b3606;
    --frame: #3b2a05;
  }
  * { box-sizing: border-box; margin: 0; padding: 0; }
  html, body { width: 1200px; height: 2358px; overflow: hidden; }
  body { font-family: "Poppins", sans-serif; color: var(--ink); background: var(--white); position: relative; }
  .display { font-family: "Archivo", sans-serif; font-weight: 900; letter-spacing: -1px; text-transform: uppercase; line-height: 1; }

  /* Hero */
  .hero { position: absolute; left: 0; top: 0; width: 1200px; height: 600px;
    background: radial-gradient(ellipse at 70% 55%, var(--olive-light) 0%, var(--olive) 40%, var(--olive-deep) 100%); }
  .hero__art { position: absolute; left: 622px; top: 110px; width: 550px; height: 430px;
    background: radial-gradient(ellipse at 55% 55%, rgba(150,130,60,.55), rgba(90,75,20,0) 70%); }
  .brand { position: absolute; left: 109px; top: 30px; font-family: "Archivo", sans-serif; font-weight: 900; font-size: 46px; color: var(--white); letter-spacing: -0.5px; }
  .hero__toggle { position: absolute; left: 1035px; top: 46px; width: 53px; height: 14px; }
  .hero__title { position: absolute; left: 92px; top: 268px; font-size: 58px; line-height: 69px; color: var(--white); }

  /* About */
  .about { position: absolute; left: 0; top: 600px; width: 1200px; height: 411px; background: var(--white); }
  .about__title { position: absolute; left: 96px; top: 133px; font-size: 74px; line-height: 76px; }
  .about__text { position: absolute; left: 583px; top: 125px; width: 520px; font-size: 15.5px; line-height: 27px; font-weight: 300; color: var(--muted); }

  /* Services */
  .services { position: absolute; left: 0; top: 1011px; width: 1200px; height: 527px; background: var(--cream); }
  .services__title { position: absolute; left: 94px; top: 104px; font-size: 72px; }
  .services__list { position: absolute; left: 67px; top: 216px; display: grid; grid-template-columns: repeat(4, 264px); list-style: none; }
  .service { text-align: center; }
  .service__icon { width: 87px; height: 87px; margin: 0 auto; border-radius: 50%;
    background: radial-gradient(circle at 50% 45%, #ffffff 55%, #e6e2da 100%); display: flex; align-items: center; justify-content: center; }
  .service__name { font-family: "Roboto", sans-serif; font-weight: 500; font-size: 15px; margin-top: 22px; letter-spacing: -0.2px; }
  .service__text { font-size: 13px; line-height: 20px; font-weight: 300; color: var(--muted); width: 180px; margin: 12px auto 0; }

  /* Team */
  .team { position: absolute; left: 0; top: 1538px; width: 1200px; height: 474px; background: var(--white); }
  .team__title { position: absolute; left: 94px; top: 130px; font-size: 72px; line-height: 76px; }
  .member { position: absolute; top: 77px; width: 230px; text-align: center; }
  .member__frame { position: absolute; top: 0; left: 11px; width: 220px; height: 220px; border: 2px solid var(--frame); }
  .member__photo { position: absolute; top: 16px; left: 0; width: 216px; height: 218px; background: linear-gradient(160deg, #e4e4e4, #c9c9c9); }
  .member__name { position: absolute; top: 250px; left: 0; width: 216px; font-weight: 600; font-size: 16px; }
  .member__role { position: absolute; top: 274px; left: 0; width: 216px; font-size: 13.5px; font-weight: 300; color: var(--muted); }
  .member__link { position: absolute; top: 300px; left: 98px; width: 20px; height: 20px; border-radius: 50%; background: var(--brown); }

  /* Subscribe */
  .subscribe { position: absolute; left: 0; top: 2012px; width: 1200px; height: 281px;
    background: linear-gradient(90deg, #a08a4e 0%, #5a4713 35%, #1e1603 60%, #120d02 100%); }
  .subscribe__art { position: absolute; left: 0; top: 0; width: 580px; height: 281px;
    background: radial-gradient(ellipse at 45% 45%, rgba(230,200,120,.6), rgba(80,60,15,0) 70%); }
  .subscribe__title { position: absolute; left: 593px; top: 50px; font-size: 50px; line-height: 54px; color: var(--white); }
  .subscribe__form { position: absolute; left: 593px; top: 175px; width: 430px; height: 52px; display: flex; border: 1px solid var(--white); }
  .subscribe__input { flex: 0 0 256px; background: var(--white); padding-left: 28px; display: flex; align-items: center; font-size: 15px; color: #333; }
  .subscribe__button { flex: 1; background: #3d2e04; color: var(--white); font-family: "Archivo", sans-serif; font-weight: 800; font-size: 16px; display: flex; align-items: center; justify-content: center; border-left: 2px solid var(--white); }

  /* Footer */
  .footer { position: absolute; left: 0; top: 2293px; width: 1200px; height: 65px; background: var(--white); }
  .footer__copy { position: absolute; left: 112px; top: 22px; font-family: "Roboto", sans-serif; font-size: 16px; }
  .footer__social { position: absolute; left: 931px; top: 19px; display: flex; gap: 15px; list-style: none; }
  .footer__social li { width: 28px; height: 28px; border-radius: 50%; background: var(--ink); }
</style>
</head>
<body>

<header class="hero">
  <div class="hero__art" role="img" aria-label="Isometric illustration of people building a digital app with charts and plants"></div>
  <div class="brand">PLOVRAK</div>
  <svg class="hero__toggle" viewBox="0 0 53 14" aria-hidden="true">
    <rect x="0" y="0" width="53" height="1.5" fill="#fff"/>
    <rect x="10" y="6" width="43" height="1.5" fill="#fff"/>
    <rect x="17" y="12" width="36" height="1.5" fill="#fff"/>
  </svg>
  <h1 class="hero__title display">Digital<br>Transformation</h1>
</header>

<section class="about">
  <h2 class="about__title display">About<br>Plovrak</h2>
  <p class="about__text">Plovrak builds critical applications to capture new markets, create modern services and captivate our customers in new and engaging ways. Creating effective and engaging solutions that truly work has always been Plovrak's core offering and is what makes us excited to work in digital. We are a forward thinking company embracing the opportunities of digital transformation and automations.</p>
</section>

<section class="services">
  <h2 class="services__title display">Core Services</h2>
  <ul class="services__list">
    <li class="service">
      <div class="service__icon">
        <svg width="44" height="44" viewBox="0 0 44 44" fill="none" stroke="#222" stroke-width="1.4" aria-hidden="true">
          <rect x="6" y="6" width="32" height="32" stroke-dasharray="2 2"/>
          <circle cx="22" cy="22" r="9"/><circle cx="22" cy="22" r="5"/>
          <path d="M20 19.5l4 2.5-4 2.5z"/>
          <circle cx="6" cy="6" r="2"/><circle cx="38" cy="38" r="2"/>
        </svg>
      </div>
      <h3 class="service__name">BUSINESS AUTOMATION</h3>
      <p class="service__text">Lorem Ipsum is simply dummy text of the printing and typesetting industry.</p>
    </li>
    <li class="service">
      <div class="service__icon">
        <svg width="44" height="44" viewBox="0 0 44 44" fill="none" stroke="#222" stroke-width="1.4" aria-hidden="true">
          <rect x="10" y="5" width="18" height="34" rx="2"/>
          <path d="M10 10h18M10 34h18M15 17l-3 3 3 3M22 17l3 3-3 3"/>
          <circle cx="30" cy="26" r="5"/><circle cx="30" cy="26" r="1.5"/>
        </svg>
      </div>
      <h3 class="service__name">APPLICATION DEVELOPMENT</h3>
      <p class="service__text">Lorem Ipsum is simply dummy text of the printing and typesetting industry.</p>
    </li>
    <li class="service">
      <div class="service__icon">
        <svg width="44" height="44" viewBox="0 0 44 44" fill="none" stroke="#222" stroke-width="1.4" aria-hidden="true">
          <path d="M22 10l7 12-4 6h-6l-4-6z"/><circle cx="22" cy="20" r="1.5"/>
          <path d="M19 28v5h6v-5M20 33v4h4v-4"/>
          <rect x="4" y="8" width="5" height="5"/><rect x="35" y="8" width="5" height="5"/><rect x="19.5" y="4" width="5" height="5"/>
          <path d="M9 10.5q6-4 10.5-4M35 10.5q-6-4-10.5-4"/>
        </svg>
      </div>
      <h3 class="service__name">INTERFACE DESIGN AND UX</h3>
      <p class="service__text">Lorem Ipsum is simply dummy text of the printing and typesetting industry.</p>
    </li>
    <li class="service">
      <div class="service__icon">
        <svg width="44" height="44" viewBox="0 0 44 44" fill="none" stroke="#222" stroke-width="1.4" aria-hidden="true">
          <rect x="6" y="5" width="8" height="10"/><rect x="30" y="5" width="10" height="7"/>
          <path d="M15 26a5 5 0 0 1 5-6 6 6 0 0 1 11 2 4 4 0 0 1 0 8H17a4 4 0 0 1-2-4z"/>
          <rect x="6" y="32" width="9" height="6"/><rect x="32" y="32" width="7" height="8"/>
          <path d="M10 15v9h5M35 12v10M10 32v-2h7M35 32v-2"/>
        </svg>
      </div>
      <h3 class="service__name">ENTERPRISE INTEGRATIONS</h3>
      <p class="service__text">Lorem Ipsum is simply dummy text of the printing and typesetting industry.</p>
    </li>
  </ul>
</section>

<section class="team">
  <h2 class="team__title display">Our Team<br>Members</h2>
  <article class="member" style="left:570px">
    <div class="member__frame"></div>
    <div class="member__photo" role="img" aria-label="Portrait photo of Torvald Bergqvist in a dark suit"></div>
    <h3 class="member__name">TORVALD BERGQVIST</h3>
    <p class="member__role">Position Name</p>
    <a class="member__link" href="https://www.netlinkpro.example/company/74819203/admin/" aria-label="Profile"></a>
  </article>
  <article class="member" style="left:870px">
    <div class="member__frame"></div>
    <div class="member__photo" role="img" aria-label="Portrait photo of Mikael Dahlgren in a navy suit"></div>
    <h3 class="member__name">MIKAEL DAHLGREN</h3>
    <p class="member__role">Position Name</p>
    <a class="member__link" href="https://www.netlinkpro.example/company/74819203/admin/" aria-label="Profile"></a>
  </article>
</section>

<section class="subscribe">
  <div class="subscribe__art" role="img" aria-label="Photo of a hand touching a glowing golden network"></div>
  <h2 class="subscribe__title display">Subscribe for our<br>latest updates</h2>
  <div class="subscribe__form">
    <div class="subscribe__input">Email Address</div>
    <div class="subscribe__button">SUBSCRIBE NOW</div>
  </div>
</section>

<footer class="footer">
  <p class="footer__copy">Copyright © 2022 Plovrak | All Rights Reserved</p>
  <ul class="footer__social" aria-label="Social links">
    <li></li><li></li><li></li><li></li>
  </ul>
</footer>

</body>
</html>
```